IT Business Card --- Quorvatek
Business card information technology
Professional
Mira Dunst
Senior System Consultant
47 Fernbrook Cres
Richmond Hill, L3K2P9
Ontario, Canada.
mira.dunst@quorvatekhub.com
www.quorvatekhub.com
PNXA #4183 Voice, R&S
This is my logo in AI format

```html
<!DOCTYPE html>
<html lang="en">
<head>
<meta charset="utf-8">
<title>Quorvatek Business Card</title>
<link href="https://fonts.googleapis.com/css2?family=Open+Sans:wght@400;600;700&display=swap" rel="stylesheet">
<style>
  :root{
    --bg:#e9e9ea;
    --card:#ffffff;
    --red:#c8161d;
    --red-dark:#8e0c11;
    --red-light:#e0454a;
    --ink:#4a4a4a;
    --muted:#7a7a7a;
  }
  *{box-sizing:border-box;margin:0;padding:0}
  html,body{width:1200px;height:864px;overflow:hidden}
  body{background:var(--bg);font-family:"Open Sans",Arial,sans-serif;position:relative}
  .card{position:absolute;top:282px;width:520px;height:300px;background:var(--card);border-radius:18px;overflow:hidden;box-shadow:0 6px 18px rgba(0,0,0,.18)}
  .card--back{left:50px}
  .card--front{left:630px}

  .back-brand{position:absolute;left:0;right:0;top:92px;display:flex;flex-direction:column;align-items:center}
  .brand-mark{width:64px;height:64px;border-radius:50%;background:var(--red)}
  .back-brand .brand-name{margin-top:12px;font-size:22px;font-weight:700;color:var(--red);letter-spacing:.5px}
  .back-url{margin-top:10px;font-size:10px;color:var(--ink);letter-spacing:2px}

  .swoosh{position:absolute;inset:0}
  .person{position:absolute;right:24px;top:62px;text-align:right}
  .person-name{font-size:17px;font-weight:600;color:var(--red)}
  .person-title{font-size:11px;color:var(--muted);margin-top:2px}

  .front-brand{position:absolute;left:22px;top:160px;display:flex;align-items:center;gap:9px}
  .front-brand .brand-mark{width:34px;height:34px}
  .front-brand .brand-name{font-size:26px;font-weight:700;color:var(--red)}

  .contacts{position:absolute;left:24px;top:208px;list-style:none;font-size:10px;line-height:13px;color:var(--ink)}
  .contacts li{display:flex;align-items:flex-start;gap:7px}
  .contacts li+li{margin-top:1px}
  .icon{flex:none;width:12px;height:12px;border-radius:50%;background:var(--red);display:flex;align-items:center;justify-content:center;margin-top:0.5px}
  .icon svg{width:8px;height:8px;fill:#fff}
</style>
</head>
<body>

<section class="card card--back" aria-label="Card back">
  <div class="back-brand">
    <span class="brand-mark" aria-hidden="true"></span>
    <span class="brand-name">Quorvatek</span>
    <span class="back-url">www.quorvatekhub.com</span>
  </div>
</section>

<section class="card card--front" aria-label="Card front">
  <svg class="swoosh" viewBox="0 0 520 300" aria-hidden="true">
    <defs>
      <linearGradient id="bandFill" x1="0" y1="0" x2="1" y2="1">
        <stop offset="0" stop-color="var(--red)"/>
        <stop offset="1" stop-color="var(--red-dark)"/>
      </linearGradient>
    </defs>
    <path d="M0,0 H520 V36 C400,36 300,70 200,120 C130,155 60,152 0,150 Z" fill="url(#bandFill)"/>
    <path d="M0,138 C60,140 130,140 195,108 C290,60 400,26 520,24" fill="none" stroke="var(--red-light)" stroke-width="2" opacity=".7"/>
  </svg>

  <div class="person">
    <div class="person-name">Mira Dunst</div>
    <div class="person-title">Senior System Consultant</div>
  </div>

  <div class="front-brand">
    <span class="brand-mark" aria-hidden="true"></span>
    <span class="brand-name">Quorvatek</span>
  </div>

  <ul class="contacts">
    <li>
      <span class="icon"><svg viewBox="0 0 10 10"><path d="M5 0.5a3.2 3.2 0 0 0-3.2 3.2C1.8 6.2 5 9.5 5 9.5s3.2-3.3 3.2-5.8A3.2 3.2 0 0 0 5 0.5zm0 4.4a1.2 1.2 0 1 1 0-2.4 1.2 1.2 0 0 1 0 2.4z"/></svg></span>
      <span>47 Fernbrook Cres<br>Richmond Hill, L3K2P9<br>Ontario, Canada.</span>
    </li>
    <li>
      <span class="icon"><svg viewBox="0 0 10 10"><path d="M2.2 1h1.6l.8 2-1 .8a5.5 5.5 0 0 0 2.6 2.6l.8-1 2 .8v1.6c0 .6-.5 1-1.1 1A8 8 0 0 1 1.2 2.1C1.2 1.5 1.6 1 2.2 1z"/></svg></span>
      <span>(905) 555-0147</span>
    </li>
    <li>
      <span class="icon"><svg viewBox="0 0 10 10"><path d="M1 2.5h8v5H1z M1 2.5l4 3 4-3" stroke="#fff" stroke-width=".9" fill="none"/></svg></span>
      <span>mira.dunst@quorvatekhub.com</span>
    </li>
    <li>
      <span class="icon"><svg viewBox="0 0 10 10"><circle cx="5" cy="5" r="3.6" stroke="#fff" stroke-width=".9" fill="none"/><path d="M1.4 5h7.2M5 1.4c-1.8 2-1.8 5.2 0 7.2M5 1.4c1.8 2 1.8 5.2 0 7.2" stroke="#fff" stroke-width=".8" fill="none"/></svg></span>
      <span>www.quorvatekhub.com</span>
    </li>
  </ul>
</section>

</body>
</html>
```